Business Cards for Tech Company - Halvera

We would like new modern business cards designed for our company. Attached are some examples of other business cards we like. <br/><br/>Info we need is: <br/>First Name, Last Name<br/>Address<br/>Store Phone<br/>Cell Phone<br/>Email Address<br/>Text Logo <br/>And Other Logo<br/>

Industry/Entity Type

Technology Equipment

Contact Information for Business Card

Please use these details as example:

Dale Morrow
Technology Specialist
Direct 555.617.2094
Phone 555-730-8186

dale.morrow@halvera.example

2971 Willet Lane
Fenwick Hollow, QX 00427

Font styles to use
Sans Serif
Other font styles liked:
• Anything easy to read and modern

Colors

Designer to choose colors to be used in the design.

Requirements
Must have
• Both Logos
• Signature as name
• Use the text logo and use the shark logo but do not use the full shark logo. Have it where it is zoomed in and is expanding out of the card.
Nice to have
• Keep it clean and modern
• We like blue, white, and black/grays.
Should not have
• Random icons for phone and address.

```html
<!DOCTYPE html>
<html lang="en">
<head>
<meta charset="utf-8">
<title>Halvera Business Card</title>
<link href="https://fonts.googleapis.com/css2?family=Exo+2:wght@400;500;700;800&display=swap" rel="stylesheet">
<style>
  :root {
    --page: #2b2d31;
    --card-white: #ffffff;
    --mesh-light: #f4f5f7;
    --mesh-mid: #eceef1;
    --brand-blue: #1a7ef2;
    --tail-gray: #6d6e70;
    --tail-light: #f7f8fa;
    --logo-ink: #1a7ef2;
    --text-on-blue: #ffffff;
  }
  * { box-sizing: border-box; margin: 0; padding: 0; }
  html, body {
    width: 1200px; height: 874px; overflow: hidden;
    background: var(--page);
    font-family: "Exo 2", sans-serif;
  }
  .canvas { position: relative; width: 1200px; height: 874px; }

  .card {
    position: absolute; left: 320px; width: 560px; height: 320px;
    border-radius: 18px; overflow: hidden;
  }
  .card--front { top: 92px; background: var(--card-white); }
  .card--back { top: 462px; background: var(--brand-blue); }

  .front__pattern {
    position: absolute; inset: 0;
    background: radial-gradient(ellipse at 60% 45%, var(--mesh-mid), var(--mesh-light) 55%, var(--card-white) 100%);
  }
  .front__logo {
    position: absolute; left: 0; right: 0; top: 128px;
    display: flex; align-items: center; justify-content: center; gap: 14px;
  }
  .logo__mark { width: 22px; height: 22px; background: var(--logo-ink); border-radius: 3px; }
  .logo__name {
    font-size: 56px; font-weight: 800; color: var(--logo-ink);
    letter-spacing: 0; line-height: 1;
  }

  .back__panel {
    position: absolute; right: 0; top: 0; width: 270px; height: 100%;
    background: linear-gradient(160deg, var(--tail-gray) 0%, var(--tail-gray) 40%, var(--tail-light) 41%, var(--tail-light) 100%);
    border-top-left-radius: 160px 320px;
  }
  .back__info {
    position: absolute; left: 38px; top: 70px; width: 250px; color: var(--text-on-blue);
  }
  .info__name {
    font-size: 27px; font-weight: 700; letter-spacing: 0.5px;
    text-transform: uppercase; line-height: 1;
  }
  .info__title { font-size: 15px; font-weight: 500; margin-top: 4px; }
  .info__address { font-size: 14px; margin-top: 14px; line-height: 1.3; }
  .info__contacts { list-style: none; margin-top: 12px; font-size: 14px; line-height: 1.35; }
  .info__contacts li { display: flex; align-items: center; gap: 8px; white-space: nowrap; }
  .info__contacts svg { width: 12px; height: 12px; fill: var(--text-on-blue); flex: none; }
</style>
</head>
<body>
<main class="canvas">
  <section class="card card--front" aria-label="Card front">
    <div class="front__pattern" role="img" aria-label="Faint network line pattern"></div>
    <div class="front__logo">
      <span class="logo__mark"></span>
      <span class="logo__name">Halvera</span>
    </div>
  </section>

  <section class="card card--back" aria-label="Card back">
    <div class="back__panel" role="img" aria-label="Large cropped brand symbol emerging from the card edge"></div>
    <div class="back__info">
      <h1 class="info__name">Dale Morrow</h1>
      <p class="info__title">Technology Specialist</p>
      <p class="info__address">2971 Willet Lane<br>Fenwick Hollow, QX 00427</p>
      <ul class="info__contacts">
        <li><svg viewBox="0 0 24 24"><path d="M6.6 10.8a15.1 15.1 0 0 0 6.6 6.6l2.2-2.2a1 1 0 0 1 1-.25 11.4 11.4 0 0 0 3.6.57 1 1 0 0 1 1 1V20a1 1 0 0 1-1 1A17 17 0 0 1 3 4a1 1 0 0 1 1-1h3.5a1 1 0 0 1 1 1c0 1.25.2 2.45.57 3.57a1 1 0 0 1-.25 1z"/></svg>555.617.2094 (Direct)</li>
        <li><svg viewBox="0 0 24 24"><path d="M6.6 10.8a15.1 15.1 0 0 0 6.6 6.6l2.2-2.2a1 1 0 0 1 1-.25 11.4 11.4 0 0 0 3.6.57 1 1 0 0 1 1 1V20a1 1 0 0 1-1 1A17 17 0 0 1 3 4a1 1 0 0 1 1-1h3.5a1 1 0 0 1 1 1c0 1.25.2 2.45.57 3.57a1 1 0 0 1-.25 1z"/></svg>555-730-8186 (Phone)</li>
        <li><svg viewBox="0 0 24 24"><path d="M2 5h20v14H2z M2 5l10 8 10-8" fill="none" stroke="#fff" stroke-width="2"/></svg>dale.morrow@halvera.example</li>
        <li><svg viewBox="0 0 24 24"><circle cx="12" cy="12" r="10"/></svg>www.halvera.example</li>
      </ul>
    </div>
  </section>
</main>
</body>
</html>
```